A Must Standout Business Card Design

I need A card that stands out from the rest. Possibly raised letters or Metallic card, Shiny or glossy, Looking for a more modern look or something throwback design would be nice. So i'm a open to different designs. I have a logo but not to happy with it. I will send it on a sample business card I do like.I might like you to tweak the designed card I am sending you. A new logo may be in order too. Make logo something that can be engraved on metal. I was thinking possibly KR in a box or KR mirror image or Backward E then a forward B in a circle. The name of my company is KR Works Inc. I designed an innovative hand tool to remove Valve Cores. I call the tool the Stem Pin Clasp. My tool grips and holds onto valve cores like no other tool does. Check it out at my website stempinclasp.com Maybe put a picture of the tool on the card raised or embossed or that spot gloss.
Updates
Everybody I must say have sent over some awesome designs! Every submission has been my favorite so I will be making my decision after the deadline. Nice work everyone!
Target Market(s)
Automotive people, People who wholesale refrigeration parts and equipment, People who use tools
Industry/Entity Type
Business
Contact Information for Business Card
KR Works Inc., 4172 Larkfield Rd. Unit C Brookvale OH 44912, Doug Whitlow President, 708-555-0193, Stempinclasp.com, Logo
Look and feel
Each slider illustrates characteristics of the customer's brand and the style your logo design should communicate.

```html
<!DOCTYPE html>
<html lang="en">
<head>
<meta charset="utf-8">
<title>KR Works Inc. — Business Card</title>
<link href="https://fonts.googleapis.com/css2?family=Montserrat:wght@600&family=Teko:wght@400;500&display=swap" rel="stylesheet">
<style>
  :root {
    --backdrop: #1a1a1a;
    --paper: #0d0d0d;
    --paper-light: #1c1c1c;
    --gold: #e39a1c;
    --gold-deep: #b8650a;
    --gold-bright: #f5c042;
  }
  * { margin: 0; padding: 0; box-sizing: border-box; }
  html, body {
    width: 1200px;
    height: 2896px;
    overflow: hidden;
    background: var(--backdrop);
  }
  .sheet {
    width: 1200px;
    height: 2896px;
    display: flex;
    flex-direction: column;
    align-items: center;
    justify-content: center;
    gap: 160px;
  }
  .card {
    position: relative;
    width: 1000px;
    height: 510px;
    background: radial-gradient(ellipse at 40% 30%, var(--paper-light), var(--paper) 75%);
    overflow: hidden;
  }
  .card-frame {
    position: absolute;
    inset: 22px;
    border: 4px solid var(--gold);
  }

  /* Front */
  .front-mark {
    position: absolute;
    left: 50%;
    top: 70px;
    width: 240px;
    height: 240px;
    transform: translateX(-50%);
    border: 6px solid var(--gold);
    display: flex;
    align-items: center;
    justify-content: center;
    font-family: "Montserrat", sans-serif;
    font-weight: 600;
    font-size: 110px;
    line-height: 1;
    color: var(--gold);
  }
  .front-name {
    position: absolute;
    left: 0;
    right: 0;
    top: 338px;
    text-align: center;
    font-family: "Montserrat", sans-serif;
    font-weight: 600;
    font-size: 52px;
    letter-spacing: 2px;
    color: var(--gold);
  }

  /* Back */
  .back-panel {
    position: absolute;
    left: 0;
    top: 0;
    bottom: 0;
    width: 333px;
    background: linear-gradient(135deg, var(--gold-deep), var(--gold) 45%, var(--gold-bright) 70%, var(--gold-deep));
  }
  .back-mark {
    position: absolute;
    left: 45px;
    top: 130px;
    width: 250px;
    height: 250px;
    border: 7px solid var(--paper);
    display: flex;
    align-items: center;
    justify-content: center;
    font-family: "Teko", sans-serif;
    font-weight: 500;
    font-size: 150px;
    line-height: 1;
    padding-top: 18px;
    color: var(--paper);
  }
  .back-frame {
    left: 333px;
  }
  .back-details {
    position: absolute;
    left: 375px;
    top: 70px;
    right: 50px;
    font-family: "Teko", sans-serif;
    color: var(--gold);
    text-transform: uppercase;
  }
  .company-name {
    font-size: 66px;
    font-weight: 500;
    line-height: 1;
    letter-spacing: 1px;
  }
  .website {
    font-size: 30px;
    line-height: 1.1;
    letter-spacing: 1px;
  }
  .address-block {
    margin-top: 110px;
    font-size: 31px;
    font-style: normal;
    font-weight: 400;
    line-height: 1.15;
    letter-spacing: 0.5px;
  }
</style>
</head>
<body>
<main class="sheet">
  <section class="card card-front" aria-label="Business card front">
    <div class="card-frame"></div>
    <div class="front-mark">KR</div>
    <p class="front-name">KR WORKS INC.</p>
  </section>

  <section class="card card-back" aria-label="Business card back">
    <div class="back-panel">
      <div class="back-mark">KR</div>
    </div>
    <div class="card-frame back-frame"></div>
    <div class="back-details">
      <h1 class="company-name">KR Works Inc.</h1>
      <p class="website">stempinclasp.com</p>
      <address class="address-block">
        4172 Larkfield Rd. Unit C Brookvale OH 44912,<br>
        Doug Whitlow President.<br>
        708-555-0193
      </address>
    </div>
  </section>
</main>
</body>
</html>
```